Utility Contractor looking for a new website

Water and wastewater utility contractor looking to create a new website that highlights our various services. We are looking for modern web presence that can be updated with current projects and new services as we grow. We have an existing logo that we would like to incorporate into the overall design of the site
Updates

Hi, Thank you for all the design submissions. I have had some time to review and have eliminated the ones I feel are not what I am looking for. Based on the designs that remain, I am looking for a clean (not to many bold colours), modern look that is not to busy (long scrolling page), Thanks, Dean

Target Market(s)

project managers, strata boards, owners, people who make decisions as to who operates their water/wastewater system

Industry/Entity Type

Utility

Font styles to use
Sans Serif

Requirements
Must have
• A min page that describes the company and what we do, A page for each of our services that outlines the service and the benefits of it. the look must be consistent throughout. additionally each service page should have some images related to the service

```html
<!DOCTYPE html>
<html lang="en">
<head>
<meta charset="utf-8">
<title>Valley Waterline Ltd. — Utility Operator &amp; Contractor</title>
<link rel="stylesheet" href="https://fonts.googleapis.com/css2?family=Raleway:wght@300;400;500;600&display=swap">
<style>
:root{
  --brand:#1f6fba;
  --brand-dark:#1a5e9f;
  --ink:#2b2b2b;
  --ink-soft:#555;
  --muted:#8a8a8a;
  --light-band:#eef2f3;
  --white:#fff;
  --footer:#0c2c4d;
  --footer-bottom:#0a2541;
  --footer-text:#c9d4df;
  --rule:#dfe4e6;
}
*{margin:0;padding:0;box-sizing:border-box}
html,body{width:1200px;height:2412px;overflow:hidden}
body{font-family:"Raleway",sans-serif;color:var(--ink);background:var(--white);position:relative}
.abs{position:absolute}
a{color:inherit;text-decoration:none}

/* top bar */
.topbar{left:0;top:0;width:1200px;height:27px;border-bottom:1px solid #eee;font-size:12px;color:var(--ink-soft)}
.social{left:43px;top:7px;display:flex;gap:14px}
.social span{width:13px;height:13px;border-radius:50%;background:#9aa3ab;display:block}
.topbar-mail{right:92px;top:6px}
.topbar-search{left:1138px;top:6px}

/* header */
.header{left:0;top:27px;width:1200px;height:67px;background:var(--white)}
.brand-name{left:43px;top:22px;font-size:20px;font-weight:600;color:var(--brand-dark);display:flex;align-items:center;gap:9px}
.brand-name i{width:18px;height:18px;border-radius:50%;background:var(--brand);display:block}
.nav{top:26px;font-size:14px;color:var(--ink)}
.nav.active{color:var(--brand)}
.nav-phone{left:1051px;top:25px;font-size:14px;color:var(--brand);display:flex;gap:6px;align-items:center}

/* hero */
.hero{left:0;top:94px;width:1200px;height:667px;background:radial-gradient(ellipse at 55% 30%,#1a8bd1 0%,#0b63a8 45%,#053d78 80%,#042d5c 100%)}
.hero-title{left:0;top:308px;width:1200px;text-align:center;font-size:56px;font-weight:500;color:var(--white);text-shadow:0 2px 6px rgba(0,0,0,.35)}
.hero-sub{left:0;top:397px;width:1200px;text-align:center;font-size:20px;line-height:29px;color:var(--white)}
.hero-btn{left:475px;top:504px;width:231px;height:46px;background:var(--brand);color:var(--white);font-size:16px;display:flex;align-items:center;justify-content:center}

/* services */
.services{left:0;top:761px;width:1200px;height:576px;background:var(--light-band)}
.brand-badge{left:244px;top:1030px;width:240px;text-align:center;font-size:22px;font-weight:500;color:var(--brand-dark)}
.brand-badge i{display:block;width:110px;height:110px;border-radius:50%;background:var(--brand);margin:0 auto 20px}
.services-title{left:614px;top:846px;font-size:29px;font-weight:400}
.service{left:614px;width:529px;height:72px}
.service-icon{left:0;top:0;width:58px;height:58px;border-radius:50%;background:var(--brand);display:flex;align-items:center;justify-content:center}
.service-name{left:75px;top:6px;font-size:18px;font-weight:500}
.service-desc{left:75px;top:32px;font-size:13px;color:var(--ink-soft)}
.service-rule{left:614px;width:529px;height:1px;background:var(--rule)}

/* projects */
.projects-title{left:0;top:1391px;width:1200px;text-align:center;font-size:29px}
.projects-sub{left:0;top:1439px;width:1200px;text-align:center;font-size:20px;line-height:24px}
.card{top:1526px;width:344px}
.card-img{width:344px;height:212px}
.card-title{margin-top:22px;font-size:14px}
.card-loc{margin-top:6px;font-size:13px;color:var(--brand)}
.card-text{margin-top:18px;font-size:13px;line-height:22px;color:var(--ink-soft)}

/* call to action */
.cta{left:0;top:1949px;width:1200px;height:134px;background:var(--light-band)}
.cta-title{left:43px;top:1988px;font-size:27px}
.cta-sub{left:43px;top:2026px;font-size:14px}
.cta-btn{left:994px;top:1987px;width:163px;height:44px;background:var(--brand);color:var(--white);font-size:15px;display:flex;align-items:center;justify-content:center}

/* footer */
.footer{left:0;top:2083px;width:1200px;height:294px;background:var(--footer)}
.foot-col{top:2141px;width:250px;color:var(--footer-text);font-size:13px}
.foot-col h4{font-size:13px;font-weight:400;letter-spacing:.5px;padding-bottom:12px;border-bottom:1px solid #22456a;margin-bottom:18px;color:var(--footer-text)}
.foot-col p{line-height:21px}
.foot-list li{list-style:none;margin-bottom:25px;font-size:12px}
.foot-list li::before{content:"›";margin-right:8px;font-weight:600}
.foot-social{display:flex;gap:17px;margin-top:22px}
.foot-social span{width:13px;height:13px;border-radius:50%;background:var(--brand);display:block}
.bottom{left:0;top:2377px;width:1200px;height:35px;background:var(--footer-bottom);color:var(--footer-text);font-size:11px}
.bottom-copy{left:43px;top:20px}
.bottom-links{right:43px;top:17px;display:flex;gap:30px;font-size:13px}
</style>
</head>
<body>

<div class="abs topbar">
  <div class="abs social"><span></span><span></span><span></span><span></span><span></span><span></span><span></span></div>
  <div class="abs topbar-mail">Mail: info@valleywaterline.com</div>
  <svg class="abs topbar-search" width="14" height="14" viewBox="0 0 14 14"><circle cx="6" cy="6" r="4.5" fill="none" stroke="#aaa" stroke-width="1.6"/><line x1="9.5" y1="9.5" x2="13" y2="13" stroke="#aaa" stroke-width="1.6"/></svg>
</div>

<header class="abs header">
  <div class="abs brand-name"><i></i>Valley Waterline Ltd.</div>
  <a class="abs nav active" style="left:345px">Home</a>
  <a class="abs nav" style="left:420px">System Operation</a>
  <a class="abs nav" style="left:573px">Fire Hydrant Maintenance</a>
  <a class="abs nav" style="left:771px">Backflow Device Testing</a>
  <a class="abs nav" style="left:963px">Contact us</a>
  <div class="abs nav-phone">
    <svg width="14" height="14" viewBox="0 0 24 24"><path fill="#1f6fba" d="M6.6 10.8a15 15 0 0 0 6.6 6.6l2.2-2.2a1 1 0 0 1 1-.25 11.4 11.4 0 0 0 3.6.57 1 1 0 0 1 1 1V20a1 1 0 0 1-1 1A17 17 0 0 1 3 4a1 1 0 0 1 1-1h3.5a1 1 0 0 1 1 1c0 1.25.2 2.45.57 3.57a1 1 0 0 1-.25 1z"/></svg>
    250 555 0142
  </div>
</header>

<section class="abs hero" role="img" aria-label="Photo of a clear blue water surface with splashing droplets"></section>
<h1 class="abs hero-title">Utility Operator &amp; Contractor</h1>
<p class="abs hero-sub">We are looking for modern web presence that can be updated<br>with current projects and new services as we grow.</p>
<a class="abs hero-btn">CHECK OUT OUR SERVICES</a>

<section class="abs services"></section>
<div class="abs brand-badge"><i></i>Valley Waterline Ltd.</div>
<h2 class="abs services-title">Our Services</h2>

<div class="abs service" style="top:933px">
  <div class="abs service-icon"><svg width="26" height="26" viewBox="0 0 24 24" fill="none" stroke="#fff" stroke-width="2"><line x1="6" y1="3" x2="6" y2="21"/><line x1="12" y1="3" x2="12" y2="21"/><line x1="18" y1="3" x2="18" y2="21"/><rect x="4" y="13" width="4" height="3" fill="#1f6fba"/><rect x="10" y="6" width="4" height="3" fill="#1f6fba"/><rect x="16" y="10" width="4" height="3" fill="#1f6fba"/></svg></div>
  <div class="abs service-name">System Operation</div>
  <div class="abs service-desc">If your system is on a BWA (Boil Water Advisory) we can help.</div>
</div>
<div class="abs service-rule" style="top:1011px"></div>
<div class="abs service" style="top:1029px">
  <div class="abs service-icon"><svg width="24" height="24" viewBox="0 0 24 24" fill="none" stroke="#fff" stroke-width="2.4" stroke-linecap="round"><path d="M14.5 6.5a4 4 0 0 1 5-5l-2.5 2.5 .5 2 2 .5 2.5-2.5a4 4 0 0 1-5 5L6 20a1.5 1.5 0 0 1-2-2z"/></svg></div>
  <div class="abs service-name">Fire Hydrant Maintenance</div>
  <div class="abs service-desc">Save Time &amp; Money In Costly Hydrant Replacement.</div>
</div>
<div class="abs service-rule" style="top:1107px"></div>
<div class="abs service" style="top:1125px">
  <div class="abs service-icon"><svg width="26" height="26" viewBox="0 0 24 24" fill="none" stroke="#fff" stroke-width="2"><circle cx="9" cy="13" r="5" stroke-dasharray="2 1.6"/><circle cx="9" cy="13" r="2"/><circle cx="17" cy="6" r="3" stroke-dasharray="1.5 1.2"/></svg></div>
  <div class="abs service-name">Backflow Device Testing</div>
  <div class="abs service-desc">We offer annual Backflow Device testing and servicing as required.</div>
</div>

<h2 class="abs projects-title">Featured Projects</h2>
<p class="abs projects-sub">We are looking for modern web presence that can be updated with<br>current projects and new services as we grow.</p>

<article class="abs card" style="left:57px">
  <div class="card-img" role="img" aria-label="Photo of crew flushing a water main beside a pickup truck" style="background:linear-gradient(180deg,#b9c6d2 0%,#8e9a8e 45%,#6f6a5f 100%)"></div>
  <div class="card-title">Spring water main flushing</div>
  <div class="card-loc">Kelowna BC</div>
  <p class="card-text">We are looking for modern web presence that can be updated with current projects and new services.</p>
</article>
<article class="abs card" style="left:427px">
  <div class="card-img" role="img" aria-label="Photo of a hydrant flushing water across a grassy field" style="background:linear-gradient(180deg,#5e7a4a 0%,#7f9a55 45%,#5d4f6a 100%)"></div>
  <div class="card-title">Much needed flushing of a water system</div>
  <div class="card-loc">North Okanagan</div>
  <p class="card-text">We are looking for modern web presence that can be updated with current projects and new services.</p>
</article>
<article class="abs card" style="left:797px">
  <div class="card-img" role="img" aria-label="Photo of an excavator laying blue pipe for a contact chamber in the forest" style="background:linear-gradient(180deg,#a9b2b8 0%,#6d7560 45%,#8a7f6c 100%)"></div>
  <div class="card-title">54 Meter contact chamber</div>
  <div class="card-loc">Kelowna BC</div>
  <p class="card-text">We are looking for modern web presence that can be updated with current projects and new services.</p>
</article>

<section class="abs cta"></section>
<h3 class="abs cta-title">Utility Operator &amp; Constructor</h3>
<p class="abs cta-sub">Design. Construction. Operation. Maintenance.</p>
<a class="abs cta-btn">Get in touch now!</a>

<footer class="abs footer"></footer>
<div class="abs foot-col" style="left:43px">
  <h4>ABOUT US</h4>
  <p>Curabitur laoreet fringilla porta. Proin dictum lacus at neque interdum tempor Lorem ipsum dolor sit amet.</p>
  <div class="foot-social"><span></span><span></span><span></span><span></span><span></span></div>
</div>
<div class="abs foot-col" style="left:327px">
  <h4>SERVICES</h4>
  <ul class="foot-list"><li>System Operation</li><li>Fire Hydrant Maintenance</li><li>Backflow Device Testing</li></ul>
</div>
<div class="abs foot-col" style="left:612px">
  <h4>Site</h4>
  <ul class="foot-list"><li>Contact us</li><li>Support</li><li>About us</li></ul>
</div>
<div class="abs foot-col" style="left:898px">
  <h4>CONTACT INFO</h4>
  <p>1180 Ridgeline Road, West Kelowna, BC<br>Phone: 250 555-0142<br>Toll free: 888 555-0199<br>Fax: 250 555-0177<br>Email: contact@valleywaterline.com</p>
</div>

<div class="abs bottom">
  <div class="abs bottom-copy">© Copyright Valley Waterline 2014. All rights reserved.</div>
  <nav class="abs bottom-links"><a>Home</a><a>Services</a><a>Contacts</a></nav>
</div>

</body>
</html>
```